DJ Promotional Flyer for Booking and promotional purposes

This promotional flyer would be used for Instagram or any other social media websites. I would like would like it to be used for booking purposes. My logo should be a big part of this flyer. As well as my contact information. Which would my email: djkvoss478@mailbright.net, Wavecrate: wavecrate.com/djkvoss, Instagram: DJMARLOKVOSS and the rest I will send by private message.

Target Market(s)

Club owners, or party promoters

Industry/Entity Type

Night Club

Font styles to use
Sans Serif

Colors

Designer to choose colors to be used in the design.

Requirements
Must have
• My logo, must bring attraction, picture attached of myself
Should not have
• Nothing that looks kidish

```html
<!DOCTYPE html>
<html lang="en">
<head>
<meta charset="UTF-8">
<title>DJ Marlo Kvoss – Booking Flyer</title>
<link href="https://fonts.googleapis.com/css2?family=Montserrat:wght@800&family=Exo+2:ital,wght@1,800;1,900&family=Oswald:wght@500&display=swap" rel="stylesheet">
<style>
  :root {
    --page-bg: #d4d4d4;
    --flyer-black: #050305;
    --brand-red: #e3202b;
    --line-red: #ff2a3a;
    --white: #ffffff;
    --silver-light: #f2f0f2;
    --silver-dark: #9c949a;
    --glow-purple: #5a1d5e;
    --glow-magenta: #b8256f;
    --glow-gold: #c98a3c;
  }
  * { margin: 0; padding: 0; box-sizing: border-box; }
  html, body {
    width: 1200px; height: 1200px; overflow: hidden;
    background: var(--page-bg);
  }
  .flyer {
    position: absolute; left: 0; top: 192px;
    width: 1200px; height: 815px;
    background:
      radial-gradient(ellipse 420px 260px at 640px 120px, rgba(201,138,60,0.35), transparent 70%),
      radial-gradient(ellipse 500px 300px at 700px 700px, rgba(184,37,111,0.45), transparent 70%),
      var(--flyer-black);
    overflow: hidden;
  }
  .headline-band {
    position: absolute; left: 420px; right: 0; top: 249px; height: 292px;
    background: var(--flyer-black);
    border-top: 6px solid var(--line-red);
    border-bottom: 6px solid var(--line-red);
  }
  .dj-photo {
    position: absolute; left: 0; top: 0; width: 640px; height: 815px;
    background:
      radial-gradient(circle 230px at 120px 170px, rgba(201,138,60,0.85), rgba(120,60,40,0.4) 60%, transparent 75%),
      radial-gradient(ellipse 330px 480px at 330px 560px, #2a1420 0%, #1a0c14 60%, transparent 85%),
      linear-gradient(180deg, #2b1420 0%, #3a1638 60%, var(--glow-purple) 100%);
    -webkit-mask-image: linear-gradient(90deg, #000 75%, transparent 100%);
            mask-image: linear-gradient(90deg, #000 75%, transparent 100%);
  }
  .brand-name {
    position: absolute; left: 548px; top: 52px;
    display: flex; align-items: center; gap: 18px;
    font-family: "Montserrat", sans-serif; font-weight: 800;
    color: var(--brand-red); line-height: 0.9;
  }
  .brand-name .brand-dj { font-size: 170px; letter-spacing: -6px; }
  .brand-name .brand-words { display: flex; flex-direction: column; font-size: 78px; gap: 10px; }
  .brand-name .brand-words span:last-child { margin-left: 14px; }
  .headline-aka {
    position: absolute; right: 52px; top: 258px;
    font-family: "Exo 2", sans-serif; font-style: italic; font-weight: 900;
    font-size: 200px; line-height: 1; letter-spacing: 2px;
    background: linear-gradient(180deg, var(--silver-light) 0%, var(--silver-dark) 55%, var(--silver-light) 100%);
    -webkit-background-clip: text; background-clip: text; color: transparent;
    filter: drop-shadow(3px 4px 0 var(--brand-red));
  }
  .headline-tagline {
    position: absolute; right: 52px; top: 440px;
    font-family: "Exo 2", sans-serif; font-style: italic; font-weight: 800;
    font-size: 74px; line-height: 1; color: var(--white);
    text-shadow: 3px 3px 0 var(--brand-red);
  }
  .details {
    position: absolute; right: 52px; top: 562px;
    text-align: right;
    font-family: "Oswald", sans-serif; font-weight: 500;
    color: var(--white); text-transform: uppercase;
  }
  .genres { font-size: 37px; line-height: 48px; }
  .phone { font-size: 40px; line-height: 50px; color: var(--brand-red); margin-top: 4px; }
  .contact-row {
    display: flex; justify-content: flex-end; align-items: center; gap: 10px;
    font-size: 24px; line-height: 38px; letter-spacing: -0.3px;
  }
  .contact-row .contact-item { display: inline-flex; align-items: center; gap: 8px; }
  .contact-row .contact-item + .contact-item { margin-left: 18px; }
  .icon { width: 26px; height: 26px; flex: none; }
</style>
</head>
<body>
  <main class="flyer">
    <div class="headline-band"></div>
    <div class="dj-photo" role="img" aria-label="Photo of the DJ wearing headphones and a cap in front of a glittering disco ball"></div>

    <h1 class="brand-name" aria-label="DJ Marlo Kvoss">
      <span class="brand-dj">DJ</span>
      <span class="brand-words"><span>MARLO</span><span>KVOSS</span></span>
    </h1>

    <p class="headline-aka">AKA</p>
    <p class="headline-tagline">YOUR FAVORITE DJ</p>

    <section class="details">
      <p class="genres">Playing your favorite hiphop, R&amp;B,<br>dancehall, soca, kompa, pop</p>
      <p class="phone">Call: (555)203-7814</p>
      <p class="contact-row">
        <span class="contact-item">
          <svg class="icon" viewBox="0 0 26 26"><circle cx="13" cy="13" r="11.5" fill="none" stroke="var(--brand-red)" stroke-width="2"/></svg>
          wavecrate.com/djkvoss
        </span>
      </p>
      <p class="contact-row">
        <span class="contact-item">
          <svg class="icon" viewBox="0 0 26 26"><circle cx="13" cy="13" r="11.5" fill="none" stroke="var(--brand-red)" stroke-width="2"/><rect x="7" y="9" width="12" height="8" fill="none" stroke="var(--brand-red)" stroke-width="1.6"/><path d="M7 9 L13 14 L19 9" fill="none" stroke="var(--brand-red)" stroke-width="1.6"/></svg>
          djkvoss478@mailbright.net
        </span>
        <span class="contact-item">
          <svg class="icon" viewBox="0 0 26 26"><circle cx="13" cy="13" r="11.5" fill="none" stroke="var(--brand-red)" stroke-width="2"/></svg>
          /DJMARLOKVOSS
        </span>
      </p>
    </section>
  </main>
</body>
</html>
```